Visitenkarten-Design für private Praxis für Sprachtherapie
Zielgruppe
Private Praxis für Sprachtherapie (Logopädie)
Aufgabenstellung
Siehe PDF der Anlage.

```html
<!DOCTYPE html>
<html lang="de">
<head>
<meta charset="utf-8">
<title>Visitenkarte – Praxis für Sprachtherapie Karla Wendorf</title>
<link rel="stylesheet" href="https://fonts.googleapis.com/css2?family=Fira+Sans+Condensed:wght@400;600&display=swap">
<style>
  :root{
    --navy:#0e3a78;
    --navy-deep:#082a5c;
    --blue-mid:#3d64a8;
    --blue-light:#c9d5ec;
    --line:#ffffff;
    --ink:#0e3a78;
    --white:#ffffff;
    --page:#ffffff;
  }
  *{box-sizing:border-box;margin:0;padding:0}
  html,body{width:1200px;height:628px;overflow:hidden;background:var(--page)}
  body{position:relative;font-family:"Fira Sans Condensed",Arial,sans-serif}

  .card{position:absolute;width:560px;height:340px;overflow:hidden}
  .card--back{left:30px;top:24px;background:var(--blue-light)}
  .card--front{left:610px;top:264px;background:linear-gradient(120deg,var(--navy) 0%,var(--navy-deep) 100%)}

  /* soft background area where the decorative pattern belongs */
  .backdrop{position:absolute;inset:0;pointer-events:none}
  .backdrop--back{width:300px;
    background:
      radial-gradient(circle at 30% 15%,rgba(255,255,255,.14) 0%,rgba(255,255,255,0) 65%),
      linear-gradient(160deg,var(--blue-mid) 0%,var(--navy) 70%,var(--navy-deep) 100%)}
  .backdrop--front{
    background:radial-gradient(circle at 78% 22%,rgba(255,255,255,.12) 0%,rgba(255,255,255,0) 60%)}

  /* appointment side */
  .appt-head{position:absolute;top:16px;font-size:17px;letter-spacing:.5px;color:var(--white)}
  .appt-head--days{left:16px;word-spacing:4px}
  .appt-head--date{left:345px}
  .appt-head--time{right:22px}
  .appt-row{position:absolute;left:0;width:560px;height:38px;border-bottom:2px solid var(--line)}
  .slots{position:absolute;left:16px;top:8px;display:flex;gap:6px}
  .slots span{width:22px;height:22px;background:var(--blue-light);opacity:.85}
  .colon{position:absolute;right:70px;top:8px;color:var(--white);font-size:18px}

  .brand{position:absolute;color:var(--ink);line-height:1.05;display:flex;align-items:center;gap:10px}
  .brand__text{font-weight:600;font-size:15px}
  .brand__name{display:block;font-size:24px;font-weight:600}
  .brand__dot{width:34px;height:34px;border-radius:50%;border:3px solid currentColor;flex:none}
  .card--back .brand{right:34px;bottom:40px}
  .card--front .brand{right:34px;top:40px;color:var(--white)}

  /* contact side */
  .holder{position:absolute;left:36px;top:146px;color:var(--white);font-size:27px;font-weight:600;letter-spacing:.5px}
  .contact{position:absolute;left:38px;top:206px;list-style:none;color:var(--white);font-size:19px}
  .contact li{display:flex;align-items:center;gap:12px;height:31px}
  .contact svg{width:17px;height:17px;fill:var(--white);flex:none}
</style>
</head>
<body>

<section class="card card--back" aria-label="Terminkarte">
  <div class="backdrop backdrop--back" role="img" aria-label="Dekoratives Kreismuster in Blautönen"></div>

  <p class="appt-head appt-head--days">MO DI MI DO FR</p>
  <p class="appt-head appt-head--date">DATUM</p>
  <p class="appt-head appt-head--time">UHRZEIT</p>

  <div class="appt-row" style="top:58px"><div class="slots"><span></span><span></span><span></span><span></span><span></span></div><span class="colon">:</span></div>
  <div class="appt-row" style="top:98px"><div class="slots"><span></span><span></span><span></span><span></span><span></span></div><span class="colon">:</span></div>
  <div class="appt-row" style="top:138px"><div class="slots"><span></span><span></span><span></span><span></span><span></span></div><span class="colon">:</span></div>
  <div class="appt-row" style="top:178px"><div class="slots"><span></span><span></span><span></span><span></span><span></span></div><span class="colon">:</span></div>

  <div class="brand">
    <p class="brand__text">Praxis für Sprachtherapie<span class="brand__name">Karla Wendorf</span></p>
    <span class="brand__dot"></span>
  </div>
</section>

<section class="card card--front" aria-label="Visitenkarte">
  <div class="backdrop backdrop--front" role="img" aria-label="Dekoratives Kreismuster in Blautönen"></div>

  <div class="brand">
    <p class="brand__text">Praxis für Sprachtherapie<span class="brand__name">Karla Wendorf</span></p>
    <span class="brand__dot"></span>
  </div>

  <h1 class="holder">KARLA WENDORF | INHABERIN</h1>

  <ul class="contact">
    <li><svg viewBox="0 0 24 24" aria-hidden="true"><path d="M12 2a7 7 0 0 0-7 7c0 5 7 13 7 13s7-8 7-13a7 7 0 0 0-7-7zm0 9.5A2.5 2.5 0 1 1 12 6.5a2.5 2.5 0 0 1 0 5z"/></svg>Ahornallee 42 | 48143 Feldhausen</li>
    <li><svg viewBox="0 0 24 24" aria-hidden="true"><path d="M6.6 10.8a15 15 0 0 0 6.6 6.6l2.2-2.2a1 1 0 0 1 1-.25 11.4 11.4 0 0 0 3.6.57 1 1 0 0 1 1 1V20a1 1 0 0 1-1 1A17 17 0 0 1 3 4a1 1 0 0 1 1-1h3.5a1 1 0 0 1 1 1c0 1.25.2 2.45.57 3.6a1 1 0 0 1-.25 1z"/></svg>05123 480912</li>
    <li><svg viewBox="0 0 24 24" aria-hidden="true"><path d="M3 5h18a1 1 0 0 1 1 1v12a1 1 0 0 1-1 1H3a1 1 0 0 1-1-1V6a1 1 0 0 1 1-1zm9 7.5L20 7H4z"/></svg>info@logopaedie-wendorf.de</li>
    <li><svg viewBox="0 0 24 24" aria-hidden="true"><path d="M12 2a10 10 0 1 0 0 20 10 10 0 0 0 0-20zm6.9 6h-3a15.7 15.7 0 0 0-1.4-3.6A8 8 0 0 1 18.9 8zM12 4c.8 1.2 1.5 2.5 1.9 4h-3.8c.4-1.5 1.1-2.8 1.9-4zM4.3 14a8 8 0 0 1 0-4h3.4a16.5 16.5 0 0 0 0 4zm.8 2h3a15.7 15.7 0 0 0 1.4 3.6A8 8 0 0 1 5.1 16zm3-8h-3a8 8 0 0 1 4.4-3.6A15.7 15.7 0 0 0 8.1 8zM12 20c-.8-1.2-1.5-2.5-1.9-4h3.8c-.4 1.5-1.1 2.8-1.9 4zm2.3-6H9.7a14.7 14.7 0 0 1 0-4h4.6a14.7 14.7 0 0 1 0 4zm.2 5.6a15.7 15.7 0 0 0 1.4-3.6h3a8 8 0 0 1-4.4 3.6zm1.8-5.6a16.5 16.5 0 0 0 0-4h3.4a8 8 0 0 1 0 4z"/></svg>logopaedie-wendorf.de</li>
  </ul>
</section>

</body>
</html>
```